One page template design

Hi creative designer, I want one single page template to use on my newly formed company.

The design most be built around the company logo (see tolvanet.com) and I would like to focus this layout around the top bar and the footer. The middle should be simple and clean for I need to use it with different pages with different functionalities.

The homepage will be used to promote services but on the footer I will place links to our online tools and future internal projects and documentations.

For the homepage I'd like to see well aligned boxes where the products and services will be places. Each project will have a logo (which you don't need to design, but the page layout should have spaces to put them on).

Many thanks.

```html
<!DOCTYPE html>
<html lang="en">
<head>
<meta charset="UTF-8">
<title>Tolvanet.com – Best, Smart &amp; Effective Solutions</title>
<link rel="stylesheet" href="https://fonts.googleapis.com/css2?family=Fredoka:wght@600&family=Arimo:wght@400;700&display=swap">
<style>
  :root {
    --paper: #e9e2d3;
    --paper-dark: #ddd3bf;
    --brown: #4a3524;
    --green: #5aa52b;
    --green-light: #92c84a;
    --green-dark: #6aa92d;
    --white: #ffffff;
    --text: #1f1f1f;
    --text-soft: #4d4d4d;
    --border: #d8d8d8;
    --soil: #4d3620;
    --grass: #7fbd2c;
  }
  * { margin: 0; padding: 0; box-sizing: border-box; }
  html, body { width: 1200px; height: 911px; overflow: hidden; }
  body {
    position: relative;
    background: radial-gradient(ellipse at 50% 40%, var(--paper) 0%, var(--paper-dark) 100%);
    font-family: "Arimo", Arial, sans-serif;
    color: var(--text);
  }

  .leaves {
    position: absolute; right: 0; top: 0; width: 312px; height: 108px;
    background: radial-gradient(ellipse at 60% 20%, #8cc255 0%, #5c9a2e 55%, rgba(92,154,46,0) 75%);
  }

  .brand {
    position: absolute; left: 76px; top: 30px;
    display: flex; align-items: center; gap: 12px;
  }
  .brand-dot { width: 44px; height: 44px; border-radius: 50%; background: #c9263a; }
  .brand-name {
    font-family: "Fredoka", "Arimo", sans-serif; font-weight: 600;
    font-size: 46px; color: var(--brown); letter-spacing: 0.5px;
  }

  .top-nav {
    position: absolute; left: 92px; top: 115px; width: 989px; height: 44px;
    background: linear-gradient(var(--green-light), var(--green-dark));
    border: 2px solid #fff; border-bottom: none;
    border-radius: 5px 5px 0 0;
    display: flex; align-items: center; padding-left: 16px;
  }
  .nav-list { display: flex; list-style: none; color: var(--white); font-size: 15px; }
  .nav-list li + li::before { content: "|"; margin: 0 15px; }
  .nav-list a { color: var(--white); text-decoration: none; text-shadow: 0 1px 1px rgba(0,0,0,0.25); }

  .content-panel {
    position: absolute; left: 83px; top: 157px; width: 1020px; height: 581px;
    background: var(--white); border-radius: 10px;
    box-shadow: 0 0 40px 10px rgba(80,60,30,0.25);
  }

  .hero-photo {
    position: absolute; left: 433px; top: 4px; width: 582px; height: 259px;
    border-radius: 0 8px 0 0;
    background: linear-gradient(90deg, rgba(255,255,255,1) 0%, #e8ebee 25%, #cfd4da 60%, #e2d4c8 85%, #f2f2f2 100%);
  }

  .hero-title {
    position: absolute; left: 38px; top: 18px;
    font-family: "Fredoka", "Arimo", sans-serif; font-weight: 600;
    font-size: 33px; line-height: 33px; color: var(--brown);
  }
  .hero-title .accent { color: var(--green); display: block; }
  .hero-text {
    position: absolute; left: 39px; top: 97px; width: 492px;
    font-size: 15.5px; line-height: 21.6px; color: var(--text);
  }

  .service-box {
    position: absolute; top: 264px; width: 232px; height: 288px;
    border: 1px solid var(--border); border-radius: 5px; overflow: hidden;
    background: var(--white);
  }
  .service-box:nth-of-type(1) { left: 26px; }
  .service-box:nth-of-type(2) { left: 273px; }
  .service-box:nth-of-type(3) { left: 521px; }
  .service-box:nth-of-type(4) { left: 768px; }
  .service-title {
    height: 44px; padding: 12px 0 0 14px;
    background: linear-gradient(#ffffff, #e9e9e9);
    border-bottom: 1px solid var(--border);
    font-size: 17px; font-weight: 700; color: #2b2119;
  }
  .service-logo {
    width: 76px; height: 76px; margin: 11px auto 0;
    border-radius: 6px;
    background: linear-gradient(135deg, #eef5c9, #b7cf6c);
  }
  .service-text {
    margin: 18px 12px 0 12px; font-size: 14.3px; line-height: 17.4px;
    text-align: justify; color: var(--text-soft);
  }
  .read-more {
    display: inline-block; margin: 12px 0 0 12px;
    width: 98px; height: 26px; line-height: 26px; text-align: center;
    border-radius: 4px; font-size: 14px; color: var(--white); text-decoration: none;
    background: linear-gradient(var(--green-light), var(--green-dark));
    box-shadow: 2px 2px 2px rgba(0,0,0,0.15);
  }

  .grass {
    position: absolute; left: 0; top: 756px; width: 1200px; height: 100px;
    background: linear-gradient(rgba(127,189,44,0) 0%, var(--grass) 35%, #69a522 80%, #4f3a22 100%);
  }
  .site-footer {
    position: absolute; left: 0; top: 855px; width: 1200px; height: 56px;
    background: var(--soil);
    color: var(--white); font-size: 14.4px;
  }
  .copyright { position: absolute; left: 88px; top: 20px; }
  .footer-nav { position: absolute; right: 93px; top: 18px; }
  .footer-nav .nav-list { font-size: 14.8px; }
  .footer-nav .nav-list li + li::before { margin: 0 10px; }
</style>
</head>
<body>
  <div class="leaves" role="img" aria-label="Green leaves hanging from the top corner"></div>

  <header class="brand">
    <span class="brand-dot"></span>
    <span class="brand-name">Tolvanet.com</span>
  </header>

  <nav class="top-nav">
    <ul class="nav-list">
      <li><a href="#">Home</a></li>
      <li><a href="#">Web Design</a></li>
      <li><a href="#">Web Development</a></li>
      <li><a href="#">Web Hosting</a></li>
      <li><a href="#">Domain Registration</a></li>
    </ul>
  </nav>

  <main class="content-panel">
    <div class="hero-photo" role="img" aria-label="Photo of a smiling businesswoman giving a thumbs up with cheering colleagues behind her"></div>
    <h1 class="hero-title">Best, Smart &amp;<span class="accent">Effective Solutions</span></h1>
    <p class="hero-text">Lorem ipsum dolor sit amet, consectetur adipiscing elit. Donec commodo aliquet orci, nec sollicitudin eros lacinia sed. Morbi hendrerit mi et arcu volutpat in dictum leo egestas. Aliquam tristique odio in elit lobortis porttitor. In egestas quam id sapien ultricies rhoncus placerat lorem rutrum. Quisque non quam in leo consectetur dignissim nec ac risus. Aliquam elementum lacus et leo dapibus porttitor.</p>

    <section class="service-box">
      <h2 class="service-title">XML Debugger</h2>
      <div class="service-logo" role="img" aria-label="Product logo: green gift box"></div>
      <p class="service-text">Morbi iaculis dolor quis sapien fringilla vol theutpat. Vestibulum a quam purus. Sed magna sem, ullamco rper id condimentum ac, imperdiet in lorem.</p>
      <a class="read-more" href="#">read more</a>
    </section>
    <section class="service-box">
      <h2 class="service-title">Reciprocal links</h2>
      <div class="service-logo" role="img" aria-label="Product logo: green gift box"></div>
      <p class="service-text">Morbi iaculis dolor quis sapien fringilla vol theutpat. Vestibulum a quam purus. Sed magna sem, ullamco rper id condimentum ac, imperdiet in lorem.</p>
      <a class="read-more" href="#">read more</a>
    </section>
    <section class="service-box">
      <h2 class="service-title">IT Sources</h2>
      <div class="service-logo" role="img" aria-label="Product logo: green gift box"></div>
      <p class="service-text">Morbi iaculis dolor quis sapien fringilla vol theutpat. Vestibulum a quam purus. Sed magna sem, ullamco rper id condimentum ac, imperdiet in lorem.</p>
      <a class="read-more" href="#">read more</a>
    </section>
    <section class="service-box">
      <h2 class="service-title">Start Crawling</h2>
      <div class="service-logo" role="img" aria-label="Product logo: green gift box"></div>
      <p class="service-text">Morbi iaculis dolor quis sapien fringilla vol theutpat. Vestibulum a quam purus. Sed magna sem, ullamco rper id condimentum ac, imperdiet in lorem.</p>
      <a class="read-more" href="#">read more</a>
    </section>
  </main>

  <div class="grass" role="img" aria-label="Band of green grass growing from the soil"></div>

  <footer class="site-footer">
    <p class="copyright">©2009-2010 Tolvanet.com - All Rights Reserved</p>
    <nav class="footer-nav">
      <ul class="nav-list">
        <li><a href="#">Home</a></li>
        <li><a href="#">Web Design</a></li>
        <li><a href="#">Web Development</a></li>
        <li><a href="#">Web Hosting</a></li>
        <li><a href="#">Domain Registration</a></li>
      </ul>
    </nav>
  </footer>
</body>
</html>
```